Lantern Across The Gap

Re-design our website www.lanternkv.org
We are a non profit catering for adults, elderly, veterans and youth in impoverished neighborhoods to improve their digital access and help them improve their lives and better our community.

I need the text on home page to stay. Its the first message vsitors shd read when they arrive on our page.

Number of Pages Required

4 page

Font styles to use
Other font styles liked:
• color and font shd be like the image attched below.

```html
<!DOCTYPE html>
<html lang="en">
<head>
<meta charset="utf-8">
<title>Lantern Across The Gap</title>
<link href="https://fonts.googleapis.com/css2?family=Jost:wght@400;500;600&display=swap" rel="stylesheet">
<style>
:root{
  --bg:#fbfdf0;
  --green:#c4dc99;
  --green-deep:#7fae3c;
  --peach:#f9cea3;
  --blue:#2f7be0;
  --sky:#9fc6e4;
  --pink:#f2a7b6;
  --ink:#2a2a2a;
  --muted:#555;
  --dark:#1f1f1f;
  --line:#b9b9b9;
  --white:#fff;
}
*{box-sizing:border-box;margin:0;padding:0}
html,body{width:1200px;height:4815px;overflow:hidden}
body{background:var(--bg);font-family:"Jost",sans-serif;color:var(--ink);position:relative}
.abs{position:absolute}
.brand{display:flex;align-items:center;gap:10px;font-weight:600;color:var(--ink);font-size:22px;line-height:1.05}
.brand-dot{width:22px;height:22px;border-radius:50%;background:var(--green-deep);flex:none}
.nav{left:462px;top:94px;display:flex;gap:40px;font-size:15px}
.nav .active{color:var(--green-deep);border-bottom:2px solid var(--green);padding-bottom:6px}
.call{left:818px;top:44px;display:flex;align-items:center;gap:10px;font-size:11px;line-height:1.2}
.call-icon{width:24px;height:24px;border-radius:50%;background:var(--green);display:flex;align-items:center;justify-content:center}
.pill{display:flex;align-items:center;justify-content:center;border-radius:30px;font-size:13px;font-weight:600;letter-spacing:.5px}
.pill.green{background:var(--green);color:#39541a}
.pill.peach{background:var(--peach);color:#6b4321}
.hero{left:0;top:0;width:1200px;height:822px;background:radial-gradient(ellipse at 50% 45%,#e8c4a8 0%,#f3dccb 35%,var(--bg) 70%)}
.hero-bucket{left:385px;top:350px;width:430px;height:250px;background:linear-gradient(#9fd14a,#7fbd2c);border-radius:18px 18px 40px 40px}
.hero-title{left:385px;top:440px;width:430px;text-align:center;color:var(--white);font-weight:600;font-size:33px;line-height:1.25;letter-spacing:.5px}
.hero-btn{left:525px;top:542px;width:154px;height:39px;background:var(--blue);color:var(--white);border-radius:30px;font-size:14px;font-weight:600}
.dots{left:1141px;top:432px;display:flex;flex-direction:column;gap:16px}
.dots span{width:10px;height:10px;border-radius:50%;background:var(--white)}
.dots .on{width:16px;height:16px;margin-left:-3px;border:3px solid var(--sky);background:var(--white)}
.h2{font-weight:600;font-size:34px;text-align:center;width:1200px;left:0;letter-spacing:.5px}
.mark{width:24px;height:24px;border-radius:50%;background:var(--green);left:588px}
.about-blob{left:75px;top:935px;width:495px;height:430px;background:linear-gradient(135deg,#c9b9a5,#8c7b69 60%,#5d6e4c);border-radius:48% 52% 45% 55%/50% 45% 55% 50%;box-shadow:-14px 18px 0 var(--green)}
.about-text{left:628px;top:1002px;width:480px}
.about-text h3{font-size:17px;font-weight:600;margin-bottom:12px}
.about-text p{font-size:13.5px;line-height:25px;color:var(--muted)}
.mv{left:628px;top:1208px;display:flex;gap:60px;font-size:15px}
.mv div{display:flex;align-items:center;gap:10px}
.rule{left:112px;width:1013px;border-top:1px dashed var(--line)}
.sub{left:0;width:1200px;text-align:center;font-size:14px;line-height:26px;color:var(--muted)}
.card{border-radius:24px;overflow:hidden}
.card-label{position:absolute;bottom:24px;width:100%;text-align:center;color:var(--white);font-size:17px;font-weight:600;letter-spacing:.3px}
.services{left:0;top:2224px;width:1200px;height:720px;background:var(--green)}
.svc{width:331px;height:447px;top:2370px;background:var(--white);border-radius:24px;overflow:hidden;text-align:center}
.svc-img{height:232px}
.svc h4{font-size:17px;font-weight:600;margin:38px 0 14px}
.svc p{font-size:12.5px;line-height:22px;color:var(--muted);padding:0 28px}
.svc-go{position:absolute;left:148px;top:400px;width:36px;height:36px;border-radius:50%;background:var(--green);display:flex;align-items:center;justify-content:center}
.explore-h{left:0;width:1200px;text-align:center;font-size:33px;font-weight:500;line-height:41px}
.circle{border-radius:50%;width:124px;height:124px;display:flex;align-items:center;justify-content:center}
.lbl{font-size:15px;font-weight:500;text-align:center;width:300px;letter-spacing:.3px}
.field{border:1px solid #9a9a9a;border-radius:4px;font-size:11px;padding:12px 14px;color:#444;background:var(--bg)}
.footer{left:0;top:4381px;width:1200px;height:363px;background:var(--dark);color:var(--white)}
.fcol h5{font-size:16px;font-weight:600;letter-spacing:.3px}
.fcol h5::after{content:"";display:block;width:38px;height:2px;background:var(--white);margin-top:10px}
.fcol ul{list-style:none;margin-top:16px;font-size:13px;line-height:27px}
.fcol li::before{content:">";margin-right:12px}
.fcol li.active{color:var(--green)}
.info{font-size:12.5px;line-height:20px;display:flex;gap:14px;margin-top:18px}
.copy{left:75px;top:4770px;font-size:12px;color:var(--ink)}
.social{top:4762px;width:34px;height:34px;border-radius:50%;background:var(--green)}
</style>
</head>
<body>

<!-- Hero -->
<div class="abs hero" role="img" aria-label="Two pairs of hands holding a green bin full of old electronics"></div>
<div class="abs hero-bucket" role="img" aria-label="Green recycling bin with discarded devices"></div>
<div class="abs hero-title">LANTERN ACROSS THE<br>GAP</div>
<div class="abs pill hero-btn">Donate</div>
<div class="abs dots"><span></span><span class="on"></span><span></span><span></span></div>

<!-- Header -->
<div class="abs brand" style="left:71px;top:52px"><span class="brand-dot"></span><span>Lantern Across<br>The Gap</span></div>
<nav class="abs nav">
  <span class="active">Home</span><span>About</span><span>Get Connected</span><span>e-Waste Services</span><span>Our Impact</span><span>Contact</span>
</nav>
<div class="abs call">
  <span class="call-icon"><svg width="12" height="12" viewBox="0 0 24 24"><path d="M6.6 10.8a15 15 0 0 0 6.6 6.6l2.2-2.2c.3-.3.7-.4 1-.2 1.1.4 2.3.6 3.6.6.6 0 1 .4 1 1V20c0 .6-.4 1-1 1A17 17 0 0 1 3 4c0-.6.4-1 1-1h3.5c.6 0 1 .4 1 1 0 1.3.2 2.5.6 3.6.1.3 0 .7-.2 1z" fill="#3b5a1a"/></svg></span>
  <span>Call Us<br>301 555 0148</span>
</div>
<div class="abs pill green" style="left:965px;top:37px;width:156px;height:38px;gap:18px">Donate
  <svg width="40" height="10" viewBox="0 0 40 10"><path d="M0 5h38M33 1l5 4-5 4" stroke="#333" stroke-width="1.5" fill="none"/></svg></div>

<!-- About -->
<div class="abs h2" style="top:890px">ABOUT US</div>
<div class="abs mark" style="top:948px"></div>
<div class="abs about-blob" role="img" aria-label="Teacher helping children working at computers in a classroom"></div>
<div class="abs about-text">
  <h3>LANTERN ACROSS THE GAP</h3>
  <p>A charitable organization, Open Horizon Initiative DBA Lantern Across The Gap, is based in Kestrel Valley, California. The focus of Lantern Across The Gap is to provide programs and services that empower and uplift people, providing the opportunity to advance their knowledge and develop lifelong skills while creating positive change. Lantern Across The Gap...</p>
</div>
<div class="abs mv">
  <div><svg width="54" height="48" viewBox="0 0 54 48" fill="none" stroke="#333" stroke-width="1.6"><path d="M2 46 20 16l8 12 6-8 18 26z"/><path d="M20 16V2h12l-3 4 3 4H20"/></svg>MISSION</div>
  <div><svg width="44" height="50" viewBox="0 0 44 50" fill="none" stroke="#333" stroke-width="1.6"><circle cx="22" cy="18" r="16"/><path d="M16 34v8h12v-8M18 47h8M16 16l6 10 6-10"/></svg>VISION</div>
</div>
<div class="abs pill green" style="left:632px;top:1290px;width:153px;height:37px">READ MORE</div>
<div class="abs pill peach" style="left:804px;top:1290px;width:153px;height:37px">DONATE</div>

<div class="abs rule" style="top:1462px"></div>

<!-- Get Connected -->
<div class="abs h2" style="top:1514px;font-weight:500">Get Connected</div>
<div class="abs sub" style="top:1554px">Give Yourself the Tools to Easily Access<br>Opportunities Online</div>

<div class="abs card" style="left:112px;top:1620px;width:310px;height:238px;background:linear-gradient(160deg,#4d6c6a,#1f3434)" role="img" aria-label="Hands on a laptop with floating document icons"><div class="card-label">GET TECHNOLOGY</div></div>
<div class="abs card" style="left:776px;top:1620px;width:310px;height:238px;background:linear-gradient(160deg,#8a8f9c,#3a3230)" role="img" aria-label="Students working at computers in a lab"><div class="card-label">TECH SUPPORT</div></div>
<div class="abs card" style="left:445px;top:1620px;width:310px;height:500px;background:linear-gradient(#e4e0dc,#f4f2ef 55%,#ffffff 80%);box-shadow:0 10px 24px rgba(0,0,0,.15)" role="img" aria-label="Young girl smiling while using a laptop"><div class="card-label" style="color:var(--ink);bottom:30px">DIGITAL TRAINING</div></div>
<div class="abs card" style="left:112px;top:1882px;width:310px;height:238px;background:linear-gradient(160deg,#3f7da0,#0f2a44)" role="img" aria-label="City skyline at night with connected network nodes"><div class="card-label">LOW-COST INTERNET</div></div>
<div class="abs card" style="left:776px;top:1882px;width:310px;height:238px;background:linear-gradient(160deg,#9a8f88,#c7a79a 60%,#6c5a52)" role="img" aria-label="Smiling woman in front of a computer class"><div class="card-label" style="bottom:32px">FOR ORGANIZATIONS</div></div>

<!-- Services -->
<div class="abs services"></div>
<div class="abs h2" style="top:2288px">OUR SERVICES</div>
<div class="abs svc" style="left:75px">
  <div class="svc-img" style="background:linear-gradient(#eef1f2,#b8c2c4 70%,#3fa045)" role="img" aria-label="Recycling bin of old computers in an empty office"></div>
  <h4>E-WASTE SERVICES</h4>
  <p>Lantern Across The Gap makes it easy for businesses and organizations across different industries to do good by diverting...</p>
  <div class="svc-go"><svg width="14" height="14" viewBox="0 0 14 14"><path d="M2 7h9M7 3l4 4-4 4" stroke="#333" stroke-width="1.8" fill="none"/></svg></div>
</div>
<div class="abs svc" style="left:434px">
  <div class="svc-img" style="background:linear-gradient(135deg,#5a5a5a,#1e1e1e 50%,#8a8a8a)" role="img" aria-label="Pile of old hard drives"></div>
  <h4>DATA DESTRUCTION</h4>
  <p>Data breaches cost companies an average of $4 million per instance and 80% of customers refuse to shop with companies...</p>
  <div class="svc-go"><svg width="14" height="14" viewBox="0 0 14 14"><path d="M2 7h9M7 3l4 4-4 4" stroke="#333" stroke-width="1.8" fill="none"/></svg></div>
</div>
<div class="abs svc" style="left:793px">
  <div class="svc-img" style="background:linear-gradient(90deg,#3b8fd8,#2a4e7a 50%,#2f6a35)" role="img" aria-label="Person loading old computers into a green bin"></div>
  <h4>TECHNOLOGY DRIVES</h4>
  <p>By hosting a Tech Drive for people at your organization or in your community, you're helping them safely dispose...</p>
  <div class="svc-go"><svg width="14" height="14" viewBox="0 0 14 14"><path d="M2 7h9M7 3l4 4-4 4" stroke="#333" stroke-width="1.8" fill="none"/></svg></div>
</div>

<!-- Explore -->
<div class="abs explore-h" style="top:3020px">Explore Opportunities Online with<br>Low-Cost Technology, Internet, Training &amp; Support</div>
<div class="abs sub" style="top:3135px;font-size:13.5px;line-height:22px;padding:0 240px">In order to comprehensively shrink the digital divide, we offer you access to low-cost computers, low-cost internet, free digital literacy training and tech support. Click the boxes below to explore how we can help you and members of your community unlock their full potential through digital technology.</div>

<div class="abs" style="left:470px;top:3232px;width:260px;height:400px;background:radial-gradient(ellipse at 50% 45%,#f4b8c6 0%,#f6d4c3 40%,transparent 70%)" role="img" aria-label="Smiling girl sitting cross-legged with an open laptop on her head"></div>

<div class="abs circle" style="left:246px;top:3246px;background:var(--green)"><svg width="60" height="56" viewBox="0 0 60 56" fill="none" stroke="#333" stroke-width="2"><rect x="6" y="8" width="48" height="32" rx="2"/><path d="M24 40v8h12v-8M18 50h24"/><circle cx="30" cy="24" r="7"/><circle cx="30" cy="24" r="2"/></svg></div>
<div class="abs circle" style="left:837px;top:3246px;background:var(--peach)"><svg width="60" height="56" viewBox="0 0 60 56" fill="none" stroke="#333" stroke-width="2"><rect x="6" y="6" width="48" height="34" rx="2"/><path d="M30 10v26M12 14h14M12 20h14M12 26h14M34 14h14M34 20h14M34 26h14M24 40v8h12v-8M18 50h24"/></svg></div>
<div class="abs circle" style="left:280px;top:3433px;background:var(--sky)"><svg width="60" height="60" viewBox="0 0 60 60" fill="none" stroke="#333" stroke-width="2"><circle cx="30" cy="30" r="22"/><ellipse cx="30" cy="30" rx="10" ry="22"/><path d="M8 30h44M12 19h36M12 41h36"/></svg></div>
<div class="abs circle" style="left:792px;top:3429px;background:var(--pink)"><svg width="60" height="60" viewBox="0 0 60 60" fill="none" stroke="#333" stroke-width="2"><path d="M12 32v-4a18 18 0 0 1 36 0v4"/><rect x="8" y="30" width="8" height="14" rx="3"/><rect x="44" y="30" width="8" height="14" rx="3"/><path d="M48 44c0 6-6 8-14 8"/><circle cx="30" cy="34" r="6"/></svg></div>

<div class="abs lbl" style="left:160px;top:3381px">AFFORDABLE TECHNOLOGY</div>
<div class="abs lbl" style="left:749px;top:3379px">DIGITAL LITERACY TRAINING</div>
<div class="abs lbl" style="left:192px;top:3573px">INTERNET ACCESS</div>
<div class="abs lbl" style="left:710px;top:3573px">TECH SUPPORT</div>

<svg class="abs" style="left:386px;top:3280px" width="100" height="50" viewBox="0 0 100 50" fill="none" stroke="#222" stroke-width="3"><path d="M4 26c20-6 30-8 40 0s12 10 20 2 12-16 24-16"/><path d="M80 6l10 6-8 8"/></svg>
<svg class="abs" style="left:722px;top:3280px" width="100" height="50" viewBox="0 0 100 50" fill="none" stroke="#222" stroke-width="3"><path d="M96 26c-20-6-30-8-40 0s-12 10-20 2S24 12 12 12"/><path d="M20 6 10 12l8 8"/></svg>
<svg class="abs" style="left:404px;top:3452px" width="70" height="40" viewBox="0 0 70 40" fill="none" stroke="#222" stroke-width="3"><path d="M4 26c10-14 18-14 24-4s14 8 28-14"/><path d="M48 6l8 2-1 9"/></svg>
<svg class="abs" style="left:718px;top:3452px" width="70" height="40" viewBox="0 0 70 40" fill="none" stroke="#222" stroke-width="3"><path d="M66 26C56 12 48 12 42 22S28 30 14 8"/><path d="M22 6l-8 2 1 9"/></svg>

<div class="abs pill green" style="left:434px;top:3646px;width:153px;height:38px">READ MORE</div>
<div class="abs pill peach" style="left:605px;top:3646px;width:154px;height:38px">DONATE</div>

<div class="abs rule" style="top:3779px"></div>

<!-- Quick contact -->
<div class="abs h2" style="top:3862px">QUICK CONTACT</div>
<div class="abs mark" style="top:3926px"></div>
<div class="abs field" style="left:235px;top:3983px;width:240px;height:45px">First Name*</div>
<div class="abs field" style="left:492px;top:3983px;width:235px;height:45px">Last Name*</div>
<div class="abs field" style="left:738px;top:3983px;width:240px;height:45px">Phone*</div>
<div class="abs field" style="left:235px;top:4041px;width:741px;height:45px;display:flex;justify-content:space-between">I'm interested in:*<svg width="10" height="8" viewBox="0 0 10 8"><path d="M1 2l4 4 4-4" stroke="#444" fill="none"/></svg></div>
<div class="abs field" style="left:235px;top:4099px;width:743px;height:138px">How can we help you today?*</div>
<div class="abs pill green" style="left:531px;top:4263px;width:153px;height:38px;font-size:11px">SUBMIT</div>

<!-- Footer -->
<footer class="abs footer">
  <div class="abs brand" style="left:75px;top:150px;color:var(--white)"><span class="brand-dot" style="background:var(--green)"></span><span>Lantern Across<br>The Gap</span></div>
  <div class="abs fcol" style="left:342px;top:92px">
    <h5>QUICK LINKS</h5>
    <ul><li class="active">Home</li><li>About</li><li>Get Connected</li><li>e-Waste Services</li><li>Our Impact</li><li>Contact</li></ul>
  </div>
  <div class="abs fcol" style="left:570px;top:92px">
    <h5>CONTACT INFO</h5>
    <div class="info"><svg width="12" height="12" viewBox="0 0 24 24"><path d="M6.6 10.8a15 15 0 0 0 6.6 6.6l2.2-2.2c.3-.3.7-.4 1-.2 1.1.4 2.3.6 3.6.6.6 0 1 .4 1 1V20c0 .6-.4 1-1 1A17 17 0 0 1 3 4c0-.6.4-1 1-1h3.5c.6 0 1 .4 1 1 0 1.3.2 2.5.6 3.6.1.3 0 .7-.2 1z" fill="#fff"/></svg>(310) 555-0148</div>
    <div class="info"><svg width="13" height="12" viewBox="0 0 24 18"><rect x="1" y="1" width="22" height="16" fill="#fff"/><path d="M1 1l11 9 11-9" stroke="#1f1f1f" fill="none" stroke-width="2"/></svg>info@lanternkv.org</div>
    <div class="info"><svg width="12" height="14" viewBox="0 0 24 30"><path d="M12 0a10 10 0 0 0-10 10c0 8 10 20 10 20s10-12 10-20A10 10 0 0 0 12 0z" fill="#fff"/><circle cx="12" cy="10" r="4" fill="#1f1f1f"/></svg>1480 Harbor View Ave,<br>Kestrel Valley, CA 90210</div>
  </div>
  <div class="abs fcol" style="left:869px;top:92px">
    <h5>LOCATION</h5>
  </div>
  <div class="abs" style="left:869px;top:138px;width:256px;height:146px;background:linear-gradient(135deg,#eef0f2,#dfe6ea)" role="img" aria-label="Street map showing the office location"></div>
</footer>

<div class="abs copy">Copyright © 2021 <b>LANTERN ACROSS THE GAP</b>. All Rights Reserved.</div>
<div class="abs social" style="left:947px"></div>
<div class="abs social" style="left:994px"></div>
<div class="abs social" style="left:1043px"></div>
<div class="abs social" style="left:1089px"></div>

</body>
</html>
```